Girls & Tween Birthday Hotspot

Looking to refresh our old business cards. We are a girls/tween birthday party store and salon specializing in princess, glamour and spa parties. I would like to maintain the same colors (hot pink and turquoise). Would like the card to be feminine, fun and glitzy..

Target Market(s)

Parents of girls and girls aged 4-14

Industry/Entity Type

Store

Font styles to use
Script

Colors
e34197
85cae6

Requirements
Must have
• name phone and address
colors of hot pink and turquoise
appointment day and time field on one side
Nice to have
• creativity
Should not have
• picture of lipstick

```html
<!DOCTYPE html>
<html lang="en">
<head>
<meta charset="utf-8">
<title>Glitter &amp; Gumdrops – Appointment Cards</title>
<link href="https://fonts.googleapis.com/css2?family=Dancing+Script:wght@700&display=swap" rel="stylesheet">
<style>
  :root{
    --hot-pink:#e34197;
    --turquoise:#85cae6;
    --blush:#f7bfd9;
    --petal:#fce6f1;
    --white:#ffffff;
    --stage:#3a302c;
    --script:'Dancing Script', cursive;
  }
  *{box-sizing:border-box;margin:0;padding:0}
  html,body{width:1200px;height:900px;overflow:hidden;background:var(--stage)}
  .canvas{position:relative;width:1200px;height:900px}
  .card{position:absolute;width:480px;height:290px;border-radius:14px;overflow:hidden;font-family:var(--script);box-shadow:0 6px 18px rgba(0,0,0,.35)}
  .row-1{top:120px}
  .row-2{top:520px}
  .col-left{left:80px}
  .col-right{left:640px}

  /* Appointment side, split layout */
  .split{background:var(--turquoise)}
  .split .contact-panel{position:absolute;left:0;top:0;width:172px;height:100%;background:var(--hot-pink);color:var(--white);padding:22px 16px}
  .contact-panel .holder-name{font-size:20px}
  .icon-badge{display:flex;align-items:center;justify-content:center;width:64px;height:36px;margin:26px 0 0 20px;background:var(--white);border-radius:14px}
  .icon-badge + .phone{font-size:17px;margin:6px 0 0 14px;letter-spacing:.5px}
  .contact-panel .address{font-size:14px;line-height:1.25;margin-top:6px}
  .ornament{position:absolute;border-radius:20px;background:linear-gradient(90deg,rgba(227,65,151,.15),rgba(227,65,151,.55),rgba(227,65,151,.15))}
  .split .ornament{left:220px;top:20px;width:200px;height:44px}
  .appt-label{position:absolute;font-size:21px;color:var(--white);padding:2px 14px}
  .split .appt-label{left:222px;top:72px;background:var(--hot-pink)}
  .field{position:absolute;font-size:21px;display:flex;align-items:baseline;gap:6px}
  .field .dots{display:inline-block;border-bottom:2px dotted currentColor;height:1px}
  .split .field{color:var(--white);left:196px}
  .split .field-date{top:140px}
  .split .field-time{top:178px}
  .split .field .dots{width:200px}
  .split .tagline{position:absolute;left:230px;top:222px;font-size:14px;color:var(--white)}

  /* Appointment side, banded layout */
  .banded{background:var(--petal)}
  .banded .top-band{position:absolute;left:0;top:0;width:100%;height:62px;background:var(--hot-pink);color:var(--white)}
  .banded .top-band .holder-name{position:absolute;right:22px;top:6px;font-size:19px}
  .banded .top-band .phone-line{position:absolute;left:20px;top:34px;font-size:16px;display:flex;align-items:center;gap:8px;color:var(--petal)}
  .banded .ornament{left:140px;top:72px;width:200px;height:44px}
  .banded .appt-label{left:150px;top:124px;background:var(--turquoise)}
  .banded .field{color:var(--turquoise)}
  .banded .field-time{left:268px;top:164px}
  .banded .field-time .dots{width:120px}
  .banded .field-date{left:36px;top:196px}
  .banded .field-date .dots{width:180px}
  .banded .address{position:absolute;left:70px;top:244px;font-size:15px;color:var(--turquoise)}

  /* Brand side */
  .brand-side{background:var(--blush);display:flex;flex-direction:column;align-items:center;justify-content:center;color:var(--hot-pink)}
  .brand-name{display:flex;align-items:center;gap:10px;font-size:44px;line-height:1}
  .brand-dot{width:18px;height:18px;border-radius:50%;background:var(--turquoise)}
  .services{font-size:22px;margin-top:18px}
  .website{font-size:22px;margin-top:10px}
</style>
</head>
<body>
<main class="canvas">

  <section class="card split row-1 col-left" aria-label="Appointment card, split layout">
    <div class="contact-panel">
      <p class="holder-name">Marisol</p>
      <div class="icon-badge">
        <svg width="26" height="20" viewBox="0 0 26 20" aria-hidden="true"><path d="M3 6c0-3 4-4 10-4s10 1 10 4v2h-5V6H8v2H3z" fill="#85cae6"/><rect x="6" y="9" width="14" height="9" rx="2" fill="#85cae6"/></svg>
      </div>
      <p class="phone">5550147823</p>
      <div class="icon-badge">
        <svg width="16" height="22" viewBox="0 0 16 22" aria-hidden="true"><path d="M8 1a7 7 0 0 1 7 7c0 5-7 13-7 13S1 13 1 8a7 7 0 0 1 7-7z" fill="#85cae6"/><circle cx="8" cy="8" r="2.6" fill="#fff"/></svg>
      </div>
      <p class="address">48 Willow Brook Rd<br>Cedar Hill New York 10000</p>
    </div>
    <div class="ornament" role="img" aria-label="Girl silhouette with script flourishes"></div>
    <p class="appt-label">Next Appointment</p>
    <p class="field field-date">Date <span class="dots"></span></p>
    <p class="field field-time">Time <span class="dots"></span></p>
    <p class="tagline">We know what girls want</p>
  </section>

  <section class="card brand-side row-1 col-right" aria-label="Brand side">
    <p class="brand-name"><span class="brand-dot"></span>Glitter &amp; Gumdrops</p>
    <p class="services">Parties • Spa • Boutique</p>
    <p class="website">www.glitter-and-gumdrops.com</p>
  </section>

  <section class="card banded row-2 col-left" aria-label="Appointment card, banded layout">
    <div class="top-band">
      <p class="holder-name">Marisol</p>
      <p class="phone-line">
        <svg width="20" height="15" viewBox="0 0 26 20" aria-hidden="true"><path d="M3 6c0-3 4-4 10-4s10 1 10 4v2h-5V6H8v2H3z" fill="#fce6f1"/><rect x="6" y="9" width="14" height="9" rx="2" fill="#fce6f1"/></svg>
        5550147823
      </p>
    </div>
    <div class="ornament" role="img" aria-label="Girl silhouette with script flourishes"></div>
    <p class="appt-label">Next Appointment</p>
    <p class="field field-time">Time <span class="dots"></span></p>
    <p class="field field-date">Date <span class="dots"></span></p>
    <p class="address">48 Willow Brook Road Cedar Hill New York 10000</p>
  </section>

  <section class="card brand-side row-2 col-right" aria-label="Brand side">
    <p class="brand-name"><span class="brand-dot"></span>Glitter &amp; Gumdrops</p>
    <p class="services">Parties • Spa • Boutique</p>
    <p class="website">www.glitter-and-gumdrops.com</p>
  </section>

</main>
</body>
</html>
```